ultra-minimalist business card

front (black background, matte):

tarik b. hosseny
writer | photographer
get@tarikhosseny.com

back (white background, matte):

a picture speaks a thousand words;
a word draws a thousand pictures.

www.tarikhosseny.com

all text should be small (white or silver - as long as it shows against the black - on the front; black or gray - as long as it shows against the white - on the back).

feel free to get creative in terms of arrangement, alignment, and font type, but remember, the overall style is minimalist, so nothing too fancy, please.

thanks.

```html
<!DOCTYPE html>
<html lang="en">
<head>
<meta charset="utf-8">
<title>tarik b. hosseny – business card</title>
<link rel="stylesheet" href="https://fonts.googleapis.com/css2?family=Questrial&display=swap">
<style>
  :root {
    --bg: #2b2b2b;
    --card-black: #1e1e1e;
    --card-white: #f6f6f4;
    --ink-light: #f2f2f2;
    --ink-silver: #d4d4d4;
    --ink-dark: #4a4a4a;
    --ink-darker: #3a3a3a;
  }
  * { margin: 0; padding: 0; box-sizing: border-box; }
  html, body {
    width: 1200px;
    height: 900px;
    overflow: hidden;
    background: var(--bg);
    font-family: "Questrial", "Century Gothic", sans-serif;
  }
  .canvas {
    position: relative;
    width: 1200px;
    height: 900px;
  }
  .card {
    position: absolute;
    left: 300px;
    width: 600px;
    height: 343px;
  }
  /* back side */
  .card--back {
    top: 88px;
    background: var(--card-white);
    color: var(--ink-dark);
  }
  .back__text {
    position: absolute;
    left: 200px;
    top: 122px;
    width: 320px;
    text-align: center;
  }
  .back__quote {
    font-size: 16px;
    line-height: 1.35;
    letter-spacing: 0.3px;
  }
  .back__web {
    margin-top: 14px;
    font-size: 17px;
    letter-spacing: 0.5px;
    color: var(--ink-darker);
  }
  /* front side */
  .card--front {
    top: 471px;
    background: var(--card-black);
    color: var(--ink-light);
  }
  .front__info {
    position: absolute;
    left: 40px;
    top: 36px;
  }
  .front__name {
    font-weight: 400;
    font-size: 28px;
    letter-spacing: 1.2px;
    line-height: 1.1;
  }
  .front__role {
    margin-top: 6px;
    font-size: 15px;
    letter-spacing: 0.5px;
    color: var(--ink-silver);
  }
  .front__email {
    margin-top: 12px;
    font-size: 17px;
    letter-spacing: 0.5px;
  }
</style>
</head>
<body>
<main class="canvas">
  <section class="card card--back" aria-label="Card back">
    <div class="back__text">
      <p class="back__quote">a picture speaks a thousand words;<br>a word draws a thousand pictures.</p>
      <p class="back__web">www.tarikhosseny.com</p>
    </div>
  </section>

  <section class="card card--front" aria-label="Card front">
    <div class="front__info">
      <h1 class="front__name">tarik b. hosseny</h1>
      <p class="front__role">Writer | Photographer</p>
      <p class="front__email">get@tarikhosseny.com</p>
    </div>
  </section>
</main>
</body>
</html>
```